Long term design collaboration - mobile app design & web app design

We are looking for a talented mobile designer to help us improve our UI & UX for mobile app and web app.

The screens that need to be redesigned are attached.

There is potentially a lot more work in future design available for the successful candidate.
The successful candidate would have to take part in daily stand-up around 3 times per week.
The successful candidate would join a dev team
We are software company that does property management

```html
<!DOCTYPE html>
<html lang="en">
<head>
<meta charset="utf-8">
<title>Tallow – Property Management Screens</title>
<link href="https://fonts.googleapis.com/css2?family=Inter:wght@400;500;600;700&display=swap" rel="stylesheet">
<style>
:root{
  --navy:#0c1a2e;
  --page:#f2f4f8;
  --white:#ffffff;
  --ink:#18202f;
  --muted:#6b7280;
  --line:#e7eaf0;
  --blue:#2553c6;
  --blue-soft:#e8eefb;
  --banner:#fcf4e4;
  --warn:#f5a524;
  --danger:#e0262c;
  --avatar:#c24ea9;
  --green:#1f9d55;
  --green-soft:#e3f6ea;
  --hover:#eef0f4;
  --scrim:#c6cbd5;
}
*{box-sizing:border-box}
html,body{margin:0;padding:0;overflow:hidden;background:#fff}
body{font-family:"Inter",Arial,sans-serif;color:var(--ink)}
.canvas{position:relative;width:1200px;height:597px;overflow:hidden;background:#fff}
.stage{position:absolute;left:0;top:0;width:2576px;height:1282px;transform:scale(0.46584);transform-origin:0 0}
.ic{width:12px;height:12px;fill:none;stroke:currentColor;stroke-width:1.8;stroke-linecap:round;stroke-linejoin:round;flex:none}

/* screens */
.screen{position:absolute;background:var(--page);overflow:hidden;border-radius:8px;border:1px solid #dde1e8}
.topbar{position:absolute;left:0;top:0;right:0;height:40px;background:var(--navy);color:#fff}
.brand{position:absolute;left:13px;top:10px;font-size:16px;font-weight:600;letter-spacing:0;color:#fff}
.bell{position:absolute;top:13px;width:13px;height:13px;color:#fff}
.bell-dot{position:absolute;width:5px;height:5px;border-radius:50%;background:var(--warn)}
.avatar{position:absolute;width:20px;height:20px;border-radius:50%;background:var(--avatar);color:#fff;font-size:7.5px;font-weight:600;display:flex;align-items:center;justify-content:center}
.user{position:absolute;top:11px;line-height:1.2}
.user b{display:block;font-size:8.5px;font-weight:500;color:#fff}
.user span{display:block;font-size:6.8px;color:#9aa4b6}
.logout{position:absolute;top:13px;width:13px;height:13px;color:#fff}

.sidebar{position:absolute;left:0;top:40px;bottom:0;width:37px;background:#f7f8fb;border-right:1px solid var(--line)}
.side-ic{position:absolute;left:5px;width:27px;height:20px;display:flex;align-items:center;justify-content:center;color:#4a5466;border-radius:3px}
.side-ic.active{background:var(--blue);color:#fff}

.page-title{position:absolute;font-size:17px;font-weight:600;margin:0}
.btn{position:absolute;border-radius:3px;font-size:8.5px;font-weight:600;display:flex;align-items:center;justify-content:center}
.btn-primary{background:var(--blue);color:#fff}
.btn-outline{background:#fff;color:var(--blue);border:1px solid #d5dbe6}

.setup{position:absolute;left:134px;top:92px;width:568px;height:75px;background:var(--banner);border-radius:4px}
.setup-title{position:absolute;left:12px;top:8px;display:flex;align-items:center;gap:8px;font-size:9.5px;font-weight:600}
.setup-title .ic{color:var(--danger);width:11px;height:11px}
.setup-step{position:absolute;top:30px;height:38px;background:#fff;border-radius:3px;font-size:8.5px;font-weight:500;padding:8px 20px 0 12px;line-height:1.25}
.setup-step::after,.row::after,.fin-card::after,.fin-head::after{content:"";position:absolute;right:12px;top:50%;width:4.5px;height:4.5px;border-top:1.4px solid var(--blue);border-right:1.4px solid var(--blue);transform:translateY(-50%) rotate(45deg)}

.tabs{position:absolute;left:134px;top:180px;width:568px;height:25px;border-bottom:1px solid var(--line)}
.tab{position:absolute;top:0;height:25px;display:flex;align-items:center;gap:8px;font-size:8.5px;font-weight:500;color:var(--muted)}
.tab.active{color:var(--ink);border-bottom:2px solid var(--blue);justify-content:center}
.tab .ic{width:11px;height:11px}

.card{position:absolute;background:#fff;border-radius:4px}
.card h3{margin:0;height:32px;line-height:32px;padding-left:13px;font-size:12.5px;font-weight:600}
.row{position:relative;margin:0 13px;border-top:1px solid var(--line);height:43px;padding-left:20px;display:flex;flex-direction:column;justify-content:center}
.row b{font-size:9px;font-weight:500;line-height:1.2}
.row span{font-size:8.3px;color:var(--muted);margin-top:3px;line-height:1.25}
.row::after{right:6px}
.dot{position:absolute;left:1px;top:50%;width:8px;height:8px;margin-top:-4px;border-radius:50%}
.dot.warn{background:var(--warn)}
.dot.danger{background:var(--danger)}

/* dropdown navigation */
.nav-panel{position:absolute;left:0;top:40px;width:165px;bottom:0;background:#fff;padding-top:4px;border-right:1px solid var(--line)}
.nav-item{height:26px;margin:0 4px 3px;border-radius:3px;padding-left:8px;display:flex;align-items:center;gap:8px;font-size:8.5px;color:#3b4456}
.nav-item .ic{color:#525c6e}
.nav-item.active{background:var(--blue);color:#fff}
.nav-item.active .ic{color:#fff}
.nav-item.hover{background:var(--hover)}

/* finances */
.back{position:absolute;width:13px;height:13px;color:#4a5466}
.fin-card{position:absolute;top:92px;height:40px;background:#fff;border-radius:4px;padding:8px 0 0 13px}
.fin-card b{display:block;font-size:9.5px;font-weight:600}
.fin-card span{display:block;font-size:6.8px;color:var(--muted);margin-top:3px}
.pill{position:absolute;top:13px;right:30px;background:var(--green-soft);color:var(--green);font-size:7px;font-weight:500;border-radius:8px;padding:3px 7px}

/* phones */
.phone{position:absolute;top:787px;width:208px;height:450px;background:var(--page);overflow:hidden;border-radius:10px;border:1px solid #dde1e8}
.status{position:absolute;left:0;top:0;right:0;height:60px;background:var(--navy);color:#fff}
.time{position:absolute;left:17px;top:7px;font-size:8px;font-weight:600}
.sys{position:absolute;right:12px;top:8px;display:flex;gap:3px;align-items:center}
.phone .bell{top:34px;left:149px;width:13px;height:13px}
.phone .bell-dot{left:160px;top:32px}
.phone .avatar{left:178px;top:31px;width:18px;height:18px;font-size:7px}
.lead{position:absolute;left:10px;top:35px;width:12px;height:12px;color:#fff}
.m-title{position:absolute;left:11px;top:73px;margin:0;font-size:15px;font-weight:600}
.m-card{position:absolute;left:11px;width:185px;background:#fff;border-radius:4px}
.m-card h3{margin:0;height:31px;line-height:31px;padding-left:11px;font-size:10.5px;font-weight:600}
.m-card .row{margin:0 11px;padding-left:19px}
.m-card .row.tall{height:54px}
.home-ind{position:absolute;left:65px;bottom:7px;width:76px;height:3px;border-radius:2px;background:var(--navy)}

.fin-block{position:relative;margin:0 10px;border-top:1px solid var(--line);padding:8px 0 6px}
.fin-head{position:relative;font-size:8.5px;font-weight:500;height:14px;line-height:14px}
.fin-head::after{right:6px}
.fin-line{display:flex;align-items:center;height:22px;font-size:8.2px;color:var(--muted)}
.fin-line .ic{width:10px;height:10px;margin-left:1px;color:#8a93a3}
.fin-line .k{width:56px;padding-left:11px}
.fin-line .v{color:#3b4456}

.question{height:30px;line-height:30px;padding-left:10px;font-size:9px;font-weight:500;border-bottom:1px solid var(--line)}
.option{display:flex;align-items:center;gap:8px;padding:0 14px 0 11px;font-size:8.2px;color:#3b4456;line-height:1.3}
.radio{width:11px;height:11px;border-radius:50%;border:1px solid #9aa2b1;flex:none;background:#fff}
.radio.on{border:1.5px solid var(--blue);box-shadow:inset 0 0 0 2px #fff;background:var(--blue)}

.drawer{position:absolute;left:0;top:60px;width:166px;bottom:0;background:#fff}
.drawer .brand{position:static;display:block;color:var(--navy);padding:9px 0 0 12px;height:40px;font-size:15px}
.drawer .close{position:absolute;left:144px;top:11px;width:12px;height:12px;color:#4a5466}
.scrim{position:absolute;left:166px;top:60px;right:0;bottom:0;background:var(--scrim)}
.scrim-card{position:absolute;left:0;width:30px;background:#d3d7df}
.scrim-btn{position:absolute;left:1px;top:334px;width:30px;height:24px;background:#2d4c96;border-radius:0 3px 3px 0}
</style>
</head>
<body>
<svg width="0" height="0" style="position:absolute" aria-hidden="true">
  <defs>
    <symbol id="i-users" viewBox="0 0 24 24"><circle cx="9" cy="8" r="3.5"/><path d="M3 20c0-3.5 2.7-6 6-6s6 2.5 6 6"/><circle cx="17" cy="9" r="2.5"/><path d="M17 14c2.5 0 4 2 4 5"/></symbol>
    <symbol id="i-swap" viewBox="0 0 24 24"><path d="M4 8h15l-3-3M20 16H5l3 3"/></symbol>
    <symbol id="i-receipt" viewBox="0 0 24 24"><rect x="4" y="3" width="16" height="18" rx="2"/><path d="M9 3v18M12 8h5M12 12h5M12 16h3"/></symbol>
    <symbol id="i-clip" viewBox="0 0 24 24"><rect x="6" y="4" width="12" height="17" rx="2"/><rect x="9" y="2.5" width="6" height="3" rx="1"/><path d="M12 10v6M10 12h4"/></symbol>
    <symbol id="i-mail" viewBox="0 0 24 24"><rect x="3" y="5" width="18" height="14" rx="2"/><path d="M3 7l9 6 9-6"/></symbol>
    <symbol id="i-file" viewBox="0 0 24 24"><path d="M6 3h8l4 4v14H6zM14 3v4h4"/></symbol>
    <symbol id="i-bell" viewBox="0 0 24 24"><path d="M6 16v-5a6 6 0 0 1 12 0v5l2 2H4zM10 20a2 2 0 0 0 4 0"/></symbol>
    <symbol id="i-logout" viewBox="0 0 24 24"><path d="M10 4H5v16h5M14 8l4 4-4 4M18 12H9"/></symbol>
    <symbol id="i-home" viewBox="0 0 24 24"><path d="M4 11l8-7 8 7v9H4zM10 20v-5h4v5"/></symbol>
    <symbol id="i-mega" viewBox="0 0 24 24"><path d="M4 10v4h3l8 4V6l-8 4zM18 9v6M7 14l1 5"/></symbol>
    <symbol id="i-bank" viewBox="0 0 24 24"><path d="M3 9l9-5 9 5zM5 10v8M10 10v8M14 10v8M19 10v8M3 20h18"/></symbol>
    <symbol id="i-doc" viewBox="0 0 24 24"><rect x="5" y="3" width="14" height="18" rx="2"/><path d="M9 8h6M9 12h6M9 16h4"/></symbol>
    <symbol id="i-chart" viewBox="0 0 24 24"><path d="M4 20h16M7 17V9M12 17V5M17 17v-6"/></symbol>
    <symbol id="i-folder" viewBox="0 0 24 24"><path d="M3 6h6l2 2h10v11H3z"/></symbol>
    <symbol id="i-tag" viewBox="0 0 24 24"><path d="M9 5h11v14H9l-5-7zM9 9v6"/></symbol>
    <symbol id="i-desk" viewBox="0 0 24 24"><circle cx="12" cy="6" r="3"/><path d="M8 13h8l1 4H7zM5 21h14"/></symbol>
    <symbol id="i-box" viewBox="0 0 24 24"><path d="M12 3l8 4v10l-8 4-8-4V7zM4 7l8 4 8-4M12 11v10"/></symbol>
    <symbol id="i-gear" viewBox="0 0 24 24"><circle cx="12" cy="12" r="3"/><path d="M12 3v3M12 18v3M3 12h3M18 12h3M5.6 5.6l2.1 2.1M16.3 16.3l2.1 2.1M5.6 18.4l2.1-2.1M16.3 7.7l2.1-2.1"/></symbol>
    <symbol id="i-headset" viewBox="0 0 24 24"><path d="M4 14v-2a8 8 0 0 1 16 0v2M4 14h3v5H4zM17 14h3v5h-3z"/></symbol>
    <symbol id="i-back" viewBox="0 0 24 24"><path d="M19 12H5M11 6l-6 6 6 6"/></symbol>
    <symbol id="i-menu" viewBox="0 0 24 24"><path d="M4 6h16M4 12h16M4 18h16"/></symbol>
    <symbol id="i-close" viewBox="0 0 24 24"><path d="M6 6l12 12M18 6L6 18"/></symbol>
    <symbol id="i-grid" viewBox="0 0 24 24"><rect x="4" y="4" width="6" height="6"/><rect x="4" y="14" width="6" height="6"/><path d="M14 6h6M14 9h4M14 16h6M14 19h4"/></symbol>
    <symbol id="i-list" viewBox="0 0 24 24"><path d="M4 6h16M4 12h10M4 18h7"/><circle cx="17" cy="17" r="3"/></symbol>
    <symbol id="i-alert" viewBox="0 0 24 24"><circle cx="12" cy="12" r="9"/><path d="M12 7v6M12 16.5v.5"/></symbol>
    <symbol id="i-bill" viewBox="0 0 24 24"><rect x="3" y="5" width="18" height="14" rx="1"/><path d="M3 10h18M7 15h4"/></symbol>
  </defs>
</svg>

<div class="canvas">
<div class="stage">

  <!-- Desktop: Overview -->
  <section class="screen" style="left:45px;top:45px;width:798px;height:696px">
    <header class="topbar">
      <div class="brand">Tallow</div>
      <svg class="ic bell" style="left:598px"><use href="#i-bell"/></svg>
      <i class="bell-dot" style="left:609px;top:10px"></i>
      <div class="avatar" style="left:636px;top:9px">PL</div>
      <div class="user" style="left:667px"><b>Priya Lennox</b><span>Development Manager</span></div>
      <svg class="ic logout" style="left:773px"><use href="#i-logout"/></svg>
    </header>
    <nav class="sidebar">
      <div class="side-ic" style="top:7px"><svg class="ic"><use href="#i-users"/></svg></div>
      <div class="side-ic" style="top:36px"><svg class="ic"><use href="#i-swap"/></svg></div>
      <div class="side-ic active" style="top:65px"><svg class="ic"><use href="#i-receipt"/></svg></div>
      <div class="side-ic" style="top:94px"><svg class="ic"><use href="#i-clip"/></svg></div>
      <div class="side-ic" style="top:122px"><svg class="ic"><use href="#i-mail"/></svg></div>
      <div class="side-ic" style="top:151px"><svg class="ic"><use href="#i-file"/></svg></div>
    </nav>
    <h1 class="page-title" style="left:134px;top:54px">Overview</h1>
    <div class="btn btn-primary" style="left:655px;top:52px;width:47px;height:25px">Report</div>
    <div class="setup">
      <div class="setup-title"><svg class="ic"><use href="#i-alert"/></svg>Please complete basic setups</div>
      <div class="setup-step" style="left:12px;width:129px">Service Charge<br>Schedules</div>
      <div class="setup-step" style="left:149px;width:129px">Service Charge<br>Appointment</div>
      <div class="setup-step" style="left:286px;width:129px">Invite Residents &amp;<br>Leaseholders</div>
      <div class="setup-step" style="left:422px;width:132px">Connect Payment<br>Provider</div>
    </div>
    <div class="tabs">
      <div class="tab active" style="left:195px;width:88px"><svg class="ic"><use href="#i-grid"/></svg>Summary</div>
      <div class="tab" style="left:304px"><svg class="ic"><use href="#i-list"/></svg>Details</div>
    </div>
    <div class="card" style="left:134px;top:219px;width:277px">
      <h3>General</h3>
      <div class="row"><b>Handover Date</b><span>12 January 2023</span></div>
      <div class="row"><b>Handover Date</b><span>12 January 2023</span></div>
      <div class="row"><b>Address</b><span>24 Marlow Crescent, Leeds, LS4 2QT</span></div>
      <div class="row"><b>Section 20 Limit</b><span>£20</span></div>
    </div>
    <div class="card" style="left:134px;top:436px;width:277px">
      <h3>Compliance</h3>
      <div class="row"><b>Asbestos</b><span>NA</span></div>
      <div class="row"><i class="dot warn"></i><b>Legionellas</b><span>-</span></div>
      <div class="row"><i class="dot danger"></i><b>Drains</b><span>Overdue 10 December 2023</span></div>
      <div class="row"><b>Gutters</b><span>NA</span></div>
      <div class="row"><b>Dry Risers</b><span>NA</span></div>
    </div>
    <div class="card" style="left:424px;top:219px;width:278px">
      <h3>Insurances</h3>
      <div class="row"><b>Terrorism</b><span>NA</span></div>
      <div class="row"><b>Buildings</b><span>NA</span></div>
      <div class="row"><b>Engineering</b><span>NA</span></div>
      <div class="row"><b>D &amp; O</b><span>NA</span></div>
      <div class="row"><b>Reinstatement</b><span>NA</span></div>
    </div>
    <div class="card" style="left:424px;top:479px;width:278px">
      <h3>Service Charge</h3>
      <div class="row"><b>Year End</b><span>12 December 2024</span></div>
      <div class="row"><b>Demand Dates</b><span>NA</span></div>
    </div>
    <div class="card" style="left:424px;top:610px;width:278px">
      <h3>Cosec</h3>
      <div class="row"><b>Are we responsible?</b><span>No</span></div>
    </div>
  </section>

  <!-- Desktop: Overview with navigation open -->
  <section class="screen" style="left:889px;top:45px;width:798px;height:696px">
    <header class="topbar">
      <div class="brand">Tallow</div>
      <svg class="ic bell" style="left:598px"><use href="#i-bell"/></svg>
      <i class="bell-dot" style="left:609px;top:10px"></i>
      <div class="avatar" style="left:636px;top:9px">PL</div>
      <div class="user" style="left:667px"><b>Priya Lennox</b><span>Development Manager</span></div>
      <svg class="ic logout" style="left:773px"><use href="#i-logout"/></svg>
    </header>
    <h1 class="page-title" style="left:134px;top:54px">Overview</h1>
    <div class="btn btn-primary" style="left:655px;top:52px;width:47px;height:25px">Report</div>
    <div class="setup">
      <div class="setup-title"><svg class="ic"><use href="#i-alert"/></svg>Please complete basic setups</div>
      <div class="setup-step" style="left:12px;width:129px">Service Charge<br>Schedules</div>
      <div class="setup-step" style="left:149px;width:129px">Service Charge<br>Appointment</div>
      <div class="setup-step" style="left:286px;width:129px">Invite Residents &amp;<br>Leaseholders</div>
      <div class="setup-step" style="left:422px;width:132px">Connect Payment<br>Provider</div>
    </div>
    <div class="tabs">
      <div class="tab active" style="left:195px;width:88px"><svg class="ic"><use href="#i-grid"/></svg>Summary</div>
      <div class="tab" style="left:304px"><svg class="ic"><use href="#i-list"/></svg>Details</div>
    </div>
    <div class="card" style="left:134px;top:219px;width:277px">
      <h3>General</h3>
      <div class="row"><b>Handover Date</b><span>12 January 2023</span></div>
      <div class="row"><b>Handover Date</b><span>12 January 2023</span></div>
      <div class="row"><b>Address</b><span>24 Marlow Crescent, Leeds, LS4 2QT</span></div>
      <div class="row"><b>Section 20 Limit</b><span>£20</span></div>
    </div>
    <div class="card" style="left:134px;top:436px;width:277px">
      <h3>Compliance</h3>
      <div class="row"><b>Asbestos</b><span>NA</span></div>
      <div class="row"><b>Legionellas</b><span>-</span></div>
      <div class="row"><b>Drains</b><span>Overdue 10 December 2023</span></div>
      <div class="row"><b>Gutters</b><span>NA</span></div>
      <div class="row"><b>Dry Risers</b><span>NA</span></div>
    </div>
    <div class="card" style="left:424px;top:219px;width:278px">
      <h3>Insurances</h3>
      <div class="row"><b>Terrorism</b><span>NA</span></div>
      <div class="row"><b>Buildings</b><span>NA</span></div>
      <div class="row"><b>Engineering</b><span>NA</span></div>
      <div class="row"><b>D &amp; O</b><span>NA</span></div>
      <div class="row"><b>Reinstatement</b><span>NA</span></div>
    </div>
    <div class="card" style="left:424px;top:479px;width:278px">
      <h3>Service Charge</h3>
      <div class="row"><b>Year End</b><span>12 December 2024</span></div>
      <div class="row"><b>Demand Dates</b><span>NA</span></div>
    </div>
    <div class="card" style="left:424px;top:610px;width:278px">
      <h3>Cosec</h3>
      <div class="row"><b>Are we responsible?</b><span>No</span></div>
    </div>
    <nav class="nav-panel">
      <div class="nav-item"><svg class="ic"><use href="#i-users"/></svg>User Directory</div>
      <div class="nav-item"><svg class="ic"><use href="#i-swap"/></svg>Switch Development</div>
      <div class="nav-item active"><svg class="ic"><use href="#i-receipt"/></svg>Service Charge</div>
      <div class="nav-item"><svg class="ic"><use href="#i-clip"/></svg>Property Balance</div>
      <div class="nav-item"><svg class="ic"><use href="#i-mail"/></svg>Sending Letter</div>
      <div class="nav-item hover"><svg class="ic"><use href="#i-file"/></svg>Regular Services</div>
    </nav>
  </section>

  <!-- Desktop: Finances -->
  <section class="screen" style="left:1733px;top:45px;width:798px;height:498px">
    <header class="topbar">
      <div class="brand">Tallow</div>
      <svg class="ic bell" style="left:598px"><use href="#i-bell"/></svg>
      <i class="bell-dot" style="left:609px;top:10px"></i>
      <div class="avatar" style="left:636px;top:9px">PL</div>
      <div class="user" style="left:667px"><b>Priya Lennox</b><span>Development Manager</span></div>
      <svg class="ic logout" style="left:773px"><use href="#i-logout"/></svg>
    </header>
    <nav class="sidebar">
      <div class="side-ic" style="top:7px"><svg class="ic"><use href="#i-home"/></svg></div>
      <div class="side-ic" style="top:36px"><svg class="ic"><use href="#i-mega"/></svg></div>
      <div class="side-ic" style="top:65px"><svg class="ic"><use href="#i-bank"/></svg></div>
      <div class="side-ic" style="top:94px"><svg class="ic"><use href="#i-doc"/></svg></div>
      <div class="side-ic active" style="top:122px"><svg class="ic"><use href="#i-chart"/></svg></div>
      <div class="side-ic" style="top:151px"><svg class="ic"><use href="#i-folder"/></svg></div>
      <div class="side-ic" style="top:180px"><svg class="ic"><use href="#i-tag"/></svg></div>
      <div class="side-ic" style="top:209px"><svg class="ic"><use href="#i-desk"/></svg></div>
      <div class="side-ic" style="top:238px"><svg class="ic"><use href="#i-bell"/></svg></div>
      <div class="side-ic" style="top:267px"><svg class="ic"><use href="#i-mail"/></svg></div>
      <div class="side-ic" style="top:296px"><svg class="ic"><use href="#i-box"/></svg></div>
      <div class="side-ic" style="top:325px"><svg class="ic"><use href="#i-clip"/></svg></div>
      <div class="side-ic" style="top:354px"><svg class="ic"><use href="#i-receipt"/></svg></div>
      <div class="side-ic" style="top:383px"><svg class="ic"><use href="#i-gear"/></svg></div>
      <div class="side-ic" style="top:412px"><svg class="ic"><use href="#i-headset"/></svg></div>
    </nav>
    <svg class="ic back" style="left:104px;top:59px"><use href="#i-back"/></svg>
    <h1 class="page-title" style="left:134px;top:54px">Finances</h1>
    <div class="fin-card" style="left:134px;width:278px"><b>Sub-Account</b><span>Short description lorem ipsum dolor sitamet</span></div>
    <div class="fin-card" style="left:423px;width:278px"><b>Payment Provider</b><span>Short description lorem ipsum dolor sitamet</span><i class="pill">Connected</i></div>
  </section>

  <!-- Mobile: Development Overview -->
  <section class="phone" style="left:45px">
    <div class="status">
      <div class="time">9:41</div>
      <div class="sys"><svg width="22" height="7" viewBox="0 0 22 7"><rect x="0" y="4" width="1.5" height="3" fill="#fff"/><rect x="2.5" y="2.5" width="1.5" height="4.5" fill="#fff"/><rect x="5" y="1" width="1.5" height="6" fill="#fff"/><rect x="14" y="0.5" width="7.5" height="6" rx="1" fill="none" stroke="#fff"/><rect x="15.3" y="1.8" width="5" height="3.4" fill="#fff"/><path d="M8.5 3a4 4 0 0 1 4 0M9.5 5a1.5 1.5 0 0 1 2 0" stroke="#fff" fill="none"/></svg></div>
      <svg class="ic lead"><use href="#i-menu"/></svg>
    </div>
    <svg class="ic bell"><use href="#i-bell"/></svg><i class="bell-dot"></i>
    <div class="avatar">PL</div>
    <h1 class="m-title">Development Overview</h1>
    <div class="m-card" style="top:105px">
      <h3>General</h3>
      <div class="row"><b>Handover Date</b><span>12 January 2023</span></div>
      <div class="row"><b>Units</b><span>85</span></div>
      <div class="row tall"><b>Address</b><span>24 Marlow Crescent,<br>Leeds, LS4 2QT</span></div>
      <div class="row"><b>Section 20 Limit</b><span>£20</span></div>
    </div>
    <div class="m-card" style="top:327px;height:130px">
      <h3>Compliances</h3>
      <div class="row"><b>Asbestos</b><span>NA</span></div>
      <div class="row"><i class="dot warn"></i><b>EICR</b><span>-</span></div>
    </div>
    <div class="home-ind"></div>
  </section>

  <!-- Mobile: Finance -->
  <section class="phone" style="left:297px">
    <div class="status">
      <div class="time">9:41</div>
      <div class="sys"><svg width="22" height="7" viewBox="0 0 22 7"><rect x="0" y="4" width="1.5" height="3" fill="#fff"/><rect x="2.5" y="2.5" width="1.5" height="4.5" fill="#fff"/><rect x="5" y="1" width="1.5" height="6" fill="#fff"/><rect x="14" y="0.5" width="7.5" height="6" rx="1" fill="none" stroke="#fff"/><rect x="15.3" y="1.8" width="5" height="3.4" fill="#fff"/><path d="M8.5 3a4 4 0 0 1 4 0M9.5 5a1.5 1.5 0 0 1 2 0" stroke="#fff" fill="none"/></svg></div>
      <svg class="ic lead"><use href="#i-back"/></svg>
    </div>
    <svg class="ic bell"><use href="#i-bell"/></svg><i class="bell-dot"></i>
    <div class="avatar">PL</div>
    <h1 class="m-title">Finance</h1>
    <div class="m-card" style="top:105px">
      <h3>Accounts Receivable</h3>
      <div class="fin-block">
        <div class="fin-head">Arrears</div>
        <div class="fin-line"><svg class="ic"><use href="#i-bill"/></svg><span class="k">Total</span><span class="v">£7,268.22</span></div>
        <div class="fin-line"><svg class="ic"><use href="#i-doc"/></svg><span class="k">Bills</span><span class="v">5</span></div>
      </div>
      <div class="fin-block">
        <div class="fin-head">Unallocated Receipts</div>
        <div class="fin-line"><svg class="ic"><use href="#i-receipt"/></svg><span class="k">Total</span><span class="v">£7,268.22</span></div>
        <div class="fin-line"><svg class="ic"><use href="#i-doc"/></svg><span class="k">Receipts</span><span class="v">5</span></div>
      </div>
    </div>
    <div class="m-card" style="top:289px">
      <h3>Accounts Payable</h3>
      <div class="fin-block">
        <div class="fin-head">Invoices</div>
        <div class="fin-line"><svg class="ic"><use href="#i-bill"/></svg><span class="k">Total</span><span class="v">£4,268.78</span></div>
        <div class="fin-line"><svg class="ic"><use href="#i-doc"/></svg><span class="k">Bills</span><span class="v">5</span></div>
      </div>
    </div>
    <div class="home-ind"></div>
  </section>

  <!-- Mobile: Legionellas -->
  <section class="phone" style="left:550px">
    <div class="status">
      <div class="time">9:41</div>
      <div class="sys"><svg width="22" height="7" viewBox="0 0 22 7"><rect x="0" y="4" width="1.5" height="3" fill="#fff"/><rect x="2.5" y="2.5" width="1.5" height="4.5" fill="#fff"/><rect x="5" y="1" width="1.5" height="6" fill="#fff"/><rect x="14" y="0.5" width="7.5" height="6" rx="1" fill="none" stroke="#fff"/><rect x="15.3" y="1.8" width="5" height="3.4" fill="#fff"/><path d="M8.5 3a4 4 0 0 1 4 0M9.5 5a1.5 1.5 0 0 1 2 0" stroke="#fff" fill="none"/></svg></div>
      <svg class="ic lead"><use href="#i-back"/></svg>
    </div>
    <svg class="ic bell"><use href="#i-bell"/></svg><i class="bell-dot"></i>
    <div class="avatar">PL</div>
    <h1 class="m-title">Legionellas</h1>
    <div class="m-card" style="top:105px;height:128px">
      <div class="question">Is it required?</div>
      <div class="option" style="height:30px"><i class="radio"></i>No</div>
      <div class="option" style="height:40px"><i class="radio"></i>Yes, but I don’t have a file to upload</div>
      <div class="option" style="height:30px"><i class="radio on"></i>Yes, and I have a file to upload</div>
    </div>
    <div class="btn btn-outline" style="left:11px;top:394px;width:88px;height:24px">Previous</div>
    <div class="btn btn-primary" style="left:108px;top:394px;width:88px;height:24px">Next</div>
    <div class="home-ind"></div>
  </section>

  <!-- Mobile: Navigation drawer -->
  <section class="phone" style="left:802px">
    <div class="status">
      <div class="time">9:41</div>
      <div class="sys"><svg width="22" height="7" viewBox="0 0 22 7"><rect x="0" y="4" width="1.5" height="3" fill="#fff"/><rect x="2.5" y="2.5" width="1.5" height="4.5" fill="#fff"/><rect x="5" y="1" width="1.5" height="6" fill="#fff"/><rect x="14" y="0.5" width="7.5" height="6" rx="1" fill="none" stroke="#fff"/><rect x="15.3" y="1.8" width="5" height="3.4" fill="#fff"/><path d="M8.5 3a4 4 0 0 1 4 0M9.5 5a1.5 1.5 0 0 1 2 0" stroke="#fff" fill="none"/></svg></div>
      <svg class="ic lead"><use href="#i-back"/></svg>
    </div>
    <svg class="ic bell"><use href="#i-bell"/></svg><i class="bell-dot"></i>
    <div class="avatar">PL</div>
    <div class="scrim">
      <div class="scrim-card" style="top:45px;height:128px"></div>
      <div class="scrim-btn"></div>
    </div>
    <nav class="drawer">
      <div class="brand">Tallow</div>
      <svg class="ic close"><use href="#i-close"/></svg>
      <div class="nav-item"><svg class="ic"><use href="#i-users"/></svg>User Directory</div>
      <div class="nav-item"><svg class="ic"><use href="#i-swap"/></svg>Switch Development</div>
      <div class="nav-item active"><svg class="ic"><use href="#i-receipt"/></svg>Service Charge</div>
      <div class="nav-item"><svg class="ic"><use href="#i-clip"/></svg>Property Balance</div>
      <div class="nav-item"><svg class="ic"><use href="#i-mail"/></svg>Sending Letter</div>
      <div class="nav-item hover"><svg class="ic"><use href="#i-file"/></svg>Regular Services</div>
    </nav>
    <div class="home-ind"></div>
  </section>

</div>
</div>
</body>
</html>
```